Create for us a Shop-Stopper Business Card

We need a standout, first class business card to go along with our new brand strategy. Sleek, Contemporary and fresh.

Colors and theme must sync with our websitewww.pelvorpower.co.uk

We want a business card that has a global brand appeal. TKR Energy is a small UK renewable company that specialises in energy projects in Africa. We want a business card that has the following characteristics: Very short, precise, global, stand out, NOT TOO LOUD but contemporary. The company's colour themes are White, Grey with a hint of green.

Target Market(s)

Business exec, high net worth individuals, investors, commercial leaders, suppliers, government officials

Industry/Entity Type

Solar Energy

Contact Information for Business Card

Logo, Name, Title, Address, web address, email,

Requirements
Must have
• Logo must be sharp
Nice to have
• Adapt fonts from the logo. The large circular side of the logo at the back in a very refreshing way
Should not have
• No solar panel shapes or image.Very little black. If possible avoid black. Its not coming out nice. I think !!!

```html
<!DOCTYPE html>
<html lang="en">
<head>
<meta charset="utf-8">
<title>TKR Energy – Business Card</title>
<link rel="stylesheet" href="https://fonts.googleapis.com/css2?family=Open+Sans:ital,wght@0,400;0,600;0,700;1,600;1,700&display=swap">
<style>
  :root {
    --backdrop: #ecebe7;
    --green-deep: #0f5a2c;
    --green-mid: #1f7a3c;
    --green-bright: #2d9a46;
    --green-leaf: #7dc242;
    --green-soft: #3f9a55;
    --grey-text: #555a5e;
    --grey-dark: #44484b;
    --accent-red: #d42a2a;
    --white: #ffffff;
  }
  * { box-sizing: border-box; margin: 0; padding: 0; }
  html, body {
    width: 1200px; height: 970px; overflow: hidden;
    background: var(--backdrop);
    font-family: "Open Sans", Arial, sans-serif;
  }
  .canvas { position: relative; width: 1200px; height: 970px; }
  .card {
    position: absolute; left: 228px; width: 744px; height: 435px;
    border-radius: 16px; overflow: hidden;
    box-shadow: 0 4px 14px rgba(0,0,0,0.18);
  }
  .card-front {
    top: 31px;
    background: radial-gradient(ellipse at 25% 30%, var(--green-soft) 0%, var(--green-mid) 45%, var(--green-deep) 100%);
  }
  .card-back {
    top: 503px;
    background: linear-gradient(160deg, var(--white) 55%, #f1f1f1 80%, #dcdcdc 100%);
  }
  .social-row { position: absolute; top: 36px; right: 30px; display: flex; gap: 8px; }
  .social-row span { width: 26px; height: 26px; border-radius: 4px; background: rgba(255,255,255,0.85); }
  .front-mark {
    position: absolute; left: 28px; top: 40px; width: 370px; height: 370px;
    border-radius: 50%; background: var(--green-bright); opacity: 0.75;
  }
  .front-brand {
    position: absolute; left: 403px; top: 220px;
    font-size: 47px; font-weight: 600; letter-spacing: 1px; color: var(--white);
    line-height: 1;
  }
  .front-tagline {
    position: absolute; left: 445px; top: 278px;
    font-size: 20px; font-style: italic; font-weight: 600; color: var(--white);
    white-space: nowrap;
  }
  .front-tagline b { font-weight: 700; }
  .back-brand {
    position: absolute; left: 122px; top: 70px; display: flex; align-items: center; gap: 14px;
  }
  .back-brand .brand-dot { width: 82px; height: 82px; border-radius: 50%; background: var(--green-mid); }
  .back-brand .brand-name {
    font-size: 58px; font-weight: 600; color: var(--grey-dark); letter-spacing: 4px; line-height: 1;
  }
  .brand-rule {
    position: absolute; left: 235px; top: 149px; width: 385px; height: 3px; background: var(--accent-red);
  }
  .person { position: absolute; right: 400px; top: 235px; text-align: right; }
  .person-name { font-size: 40px; font-weight: 700; color: var(--green-mid); line-height: 1.1; }
  .person-title { font-size: 21px; font-weight: 700; color: var(--green-leaf); }
  .contact-list { position: absolute; left: 384px; top: 234px; list-style: none; }
  .contact-list li {
    display: flex; align-items: center; gap: 10px; height: 29px;
    font-size: 20px; font-weight: 600; color: var(--grey-text);
  }
  .contact-list svg { width: 18px; height: 18px; flex: none; }
</style>
</head>
<body>
<div class="canvas">

  <section class="card card-front">
    <div class="social-row"><span></span><span></span><span></span></div>
    <div class="front-mark"></div>
    <div class="front-brand">TKR ENERGY</div>
    <p class="front-tagline">“Powering What Comes <b>Next.</b>”</p>
  </section>

  <section class="card card-back">
    <div class="back-brand">
      <span class="brand-dot"></span>
      <span class="brand-name">TKR ENERGY</span>
    </div>
    <div class="brand-rule"></div>

    <div class="person">
      <h1 class="person-name">Lena Ortiz</h1>
      <p class="person-title">Sales Director</p>
    </div>

    <ul class="contact-list">
      <li>
        <svg viewBox="0 0 18 18"><rect width="18" height="18" rx="3" fill="#7dc242"/><path d="M5.5 4.5l2 2-1 1.2c.6 1.4 1.7 2.5 3 3l1.2-1 2 2-1.2 1.6c-3.6-.3-6.8-3.5-7.1-7.1z" fill="#fff"/></svg>
        555 014 2290
      </li>
      <li>
        <svg viewBox="0 0 18 18"><rect y="3" width="18" height="12" rx="1.5" fill="#7dc242"/><path d="M2 5l7 5 7-5" stroke="#fff" stroke-width="1.6" fill="none"/></svg>
        lena@tkrenergy.com
      </li>
      <li>
        <svg viewBox="0 0 18 18" fill="none" stroke="#7dc242" stroke-width="1.6"><circle cx="9" cy="9" r="7.5"/><ellipse cx="9" cy="9" rx="3.3" ry="7.5"/><path d="M1.5 9h15M3 5h12M3 13h12"/></svg>
        www.tkrenergy.com
      </li>
    </ul>
  </section>

</div>
</body>
</html>
```